Fernvale Pharmacy opening

We want to have a double sided 5.5"x8.5" flyer for a new Pharmacy opening in a well known strip mall in the neighborhood and we are planning to mail it to neighbors homes.

Want to put the outside pharmacy picture on the main side of the flyer and a coupon with 25% off towards an OTC product on the back in addition to the info below (preferably in a sort of bulletin points not a list (something like the 2 examples attached).

Colors to be red like the exterior sign and blue like the interior wall paint:

Front side should have:
Fernvale pharmacy
Your locally owned and operated pharmacy around the corner.
317-4082 Tarrow rd.
Brisket hollow plaza
T. 604 827 5530 (call or text)
F. 604-827-5532

Free prescription delivery
Text us for refills
Specialized compounding
Customized compression stockings

The back side should have:

Do you forget taking your medications! We offer multiple compliance packaging options at no additional cost.
Had shingles before or worried to have it? travelling soon? check our vaccinations options!
Suffering side effects? We are experienced to check your medications interactions & different coverage options.
Hard time monitoring your blood pressure? Trying to stop smoking? we can always help.

FEELING BETTER STARTS HERE

```html
<!DOCTYPE html>
<html lang="en">
<head>
<meta charset="utf-8">
<title>Fernvale Pharmacy – Opening Flyer</title>
<link rel="stylesheet" href="https://fonts.googleapis.com/css2?family=Montserrat:ital,wght@0,500;0,600;0,700;0,800;1,500&family=Barlow+Condensed:wght@600;700&display=swap">
<style>
  :root{
    --red:#f20000;
    --red-deep:#d90000;
    --blue:#6785cc;
    --black:#000;
    --white:#fff;
    --stage:#979797;
    --stamp:#f1f2f4;
  }
  html,body{margin:0;padding:0;width:1200px;height:1200px;overflow:hidden;background:var(--stage);}
  body{position:relative;font-family:"Montserrat",sans-serif;}
  .flyer{position:absolute;left:217px;width:766px;height:495px;overflow:hidden;background:var(--white);}
  .flyer--front{top:77px;}
  .flyer--back{top:632px;}
  .flyer__shapes{position:absolute;inset:0;width:100%;height:100%;}

  /* front */
  .brand{position:absolute;left:12px;top:44px;width:350px;display:flex;align-items:center;gap:10px;}
  .brand__dot{width:40px;height:40px;border-radius:50%;background:var(--red);flex:none;}
  .brand__name{font-weight:800;font-size:26px;line-height:1;color:var(--red);letter-spacing:.2px;}
  .headline{position:absolute;left:441px;top:26px;width:315px;margin:0;font-weight:800;font-size:27.5px;line-height:.99;color:var(--white);text-transform:uppercase;}
  .perks{position:absolute;left:441px;top:192px;margin:0;padding:0;list-style:none;color:var(--white);font-weight:500;font-size:14.6px;}
  .perks li{display:flex;align-items:center;gap:7px;height:22px;}
  .perks svg{width:11px;height:11px;flex:none;}
  .visit{position:absolute;left:441px;top:297px;width:200px;height:36px;padding-left:9px;background:var(--black);color:var(--white);font-weight:700;font-size:22px;line-height:36px;}
  .address{position:absolute;left:445px;top:340px;color:var(--white);font-weight:500;font-size:16.6px;line-height:24px;}
  .contact-line{position:absolute;left:445px;display:flex;align-items:baseline;gap:8px;color:var(--white);}
  .contact-line--phone{top:385px;}
  .contact-line--fax{top:428px;}
  .contact-line svg{width:26px;height:26px;align-self:center;}
  .contact-line__number{font-family:"Barlow Condensed",sans-serif;font-weight:700;font-size:42px;line-height:44px;letter-spacing:.5px;}
  .contact-line__note{font-size:10px;font-weight:500;}
  .coupon{position:absolute;left:260px;top:346px;width:134px;height:134px;border-radius:50%;background:var(--red);box-shadow:0 0 0 4px var(--red-deep) inset;display:flex;flex-direction:column;align-items:center;justify-content:center;color:var(--white);text-align:center;}
  .coupon__pct{font-weight:800;font-size:41px;line-height:.9;}
  .coupon__off{font-weight:800;font-size:26px;line-height:.95;}
  .coupon__item{font-family:"Barlow Condensed",sans-serif;font-weight:600;font-size:19px;line-height:1.1;}

  /* back */
  .tagline{position:absolute;left:28px;top:18px;margin:0;color:var(--white);font-weight:700;font-size:22px;letter-spacing:-.2px;line-height:36px;white-space:nowrap;}
  .mark{position:absolute;left:468px;top:22px;display:flex;align-items:center;gap:8px;}
  .mark__dot{width:78px;height:78px;border-radius:50%;background:var(--red);flex:none;}
  .mark__name{font-weight:800;font-size:15px;color:var(--red);line-height:1.1;}
  .stamp{position:absolute;left:664px;top:27px;width:70px;height:70px;background:var(--stamp);}
  .service{position:absolute;display:flex;gap:9px;color:var(--white);}
  .service__dot{width:19px;height:19px;border-radius:50%;background:var(--white);opacity:.9;flex:none;margin-top:2px;}
  .service__title{margin:0;font-weight:700;font-size:14.3px;letter-spacing:-.2px;line-height:18px;}
  .service__text{margin:0;font-weight:500;font-style:italic;font-size:10.3px;line-height:14px;}
  .service--forget{left:21px;top:325px;width:360px;}
  .service--shingles{left:21px;top:382px;width:360px;}
  .service--effects{left:387px;top:325px;width:370px;}
  .service--pressure{left:387px;top:382px;width:370px;}
  .footer-contact{position:absolute;top:452px;height:44px;display:flex;align-items:center;gap:5px;color:var(--white);}
  .footer-contact--phone{left:233px;}
  .footer-contact--fax{left:527px;}
  .footer-contact svg{width:18px;height:18px;}
  .footer-contact__number{font-weight:700;font-size:24px;letter-spacing:-.3px;}
  .footer-contact__note{font-weight:600;font-size:14px;margin-top:6px;}
</style>
</head>
<body>

<section class="flyer flyer--front">
  <svg class="flyer__shapes" viewBox="0 0 766 495" preserveAspectRatio="none" aria-hidden="true">
    <defs>
      <linearGradient id="storeTones" x1="0" y1="0" x2="0" y2="1">
        <stop offset="0" stop-color="#8a8f99"/>
        <stop offset=".45" stop-color="#c8d3dd"/>
        <stop offset=".62" stop-color="#5a5d63"/>
        <stop offset="1" stop-color="#6d6e72"/>
      </linearGradient>
    </defs>
    <rect x="0" y="0" width="380" height="131" fill="#fff"/>
    <rect x="0" y="131" width="381" height="8" fill="#000"/>
    <polygon points="364,0 374,0 433,495 423,495" fill="#000"/>
    <polygon points="374,0 766,0 766,311 411,311" fill="#f20000"/>
    <polygon points="411,311 766,311 766,495 433,495" fill="#6785cc"/>
  </svg>
  <svg class="flyer__shapes" viewBox="0 0 766 495" preserveAspectRatio="none" role="img" aria-label="Photo of the pharmacy storefront in the strip mall, glass windows with signage and parking lot in front">
    <polygon points="0,139 381,139 423,495 0,495" fill="url(#storeTones)"/>
  </svg>

  <div class="brand">
    <span class="brand__dot"></span>
    <span class="brand__name">FERNVALE PHARMACY</span>
  </div>

  <h1 class="headline">Your locally owned and operated pharmacy around the corner.</h1>

  <ul class="perks">
    <li><svg viewBox="0 0 12 12"><circle cx="6" cy="6" r="5.2" fill="none" stroke="#fff" stroke-width="1.2"/><path d="M3.6 6.2l1.7 1.6 3.2-3.4" fill="none" stroke="#fff" stroke-width="1.2"/></svg>Free prescription delivery</li>
    <li><svg viewBox="0 0 12 12"><circle cx="6" cy="6" r="5.2" fill="none" stroke="#fff" stroke-width="1.2"/><path d="M3.6 6.2l1.7 1.6 3.2-3.4" fill="none" stroke="#fff" stroke-width="1.2"/></svg>Text us for refills</li>
    <li><svg viewBox="0 0 12 12"><circle cx="6" cy="6" r="5.2" fill="none" stroke="#fff" stroke-width="1.2"/><path d="M3.6 6.2l1.7 1.6 3.2-3.4" fill="none" stroke="#fff" stroke-width="1.2"/></svg>Specialized compounding</li>
    <li><svg viewBox="0 0 12 12"><circle cx="6" cy="6" r="5.2" fill="none" stroke="#fff" stroke-width="1.2"/><path d="M3.6 6.2l1.7 1.6 3.2-3.4" fill="none" stroke="#fff" stroke-width="1.2"/></svg>Customized compression stockings</li>
  </ul>

  <div class="visit">VISIT US AT</div>
  <div class="address">317-4082 Tarrow rd.<br>Brisket Hollow Plaza</div>

  <div class="contact-line contact-line--phone">
    <svg viewBox="0 0 24 24"><path d="M6.6 2.5l3 3.6-1.9 2.4c1.2 2.6 3.2 4.7 5.8 5.9l2.4-1.9 3.6 3-1.8 3.3C10.6 19 5 13.4 3.3 4.3z" fill="#000"/><path d="M14 3.5a7 7 0 0 1 6.5 6.5M14 6.5a4 4 0 0 1 3.5 3.5" fill="none" stroke="#000" stroke-width="1.6"/></svg>
    <span class="contact-line__number">604 827 5530</span>
    <span class="contact-line__note">(call or text)</span>
  </div>
  <div class="contact-line contact-line--fax">
    <svg viewBox="0 0 24 24"><rect x="6" y="2" width="12" height="6" fill="#000"/><rect x="2" y="8" width="20" height="9" rx="2" fill="#000"/><rect x="6" y="14" width="12" height="8" fill="#000" stroke="#fff" stroke-width="1"/><path d="M8 17h8M8 19.5h8" stroke="#fff" stroke-width="1"/></svg>
    <span class="contact-line__number">604 827 5532</span>
  </div>

  <div class="coupon">
    <span class="coupon__pct">25%</span>
    <span class="coupon__off">OFF</span>
    <span class="coupon__item">AN OTC PRODUCT</span>
  </div>
</section>

<section class="flyer flyer--back">
  <svg class="flyer__shapes" viewBox="0 0 766 495" preserveAspectRatio="none" aria-hidden="true">
    <polygon points="0,0 448,0 437,64 0,64" fill="#6785cc"/>
    <rect x="0" y="312" width="766" height="183" fill="#f20000"/>
    <polygon points="209,452 766,452 766,495 201,495" fill="#000"/>
    <polygon points="0,481 203,481 201,495 0,495" fill="#fff"/>
  </svg>
  <svg class="flyer__shapes" viewBox="0 0 766 495" preserveAspectRatio="none" role="img" aria-label="Photo of the pharmacy interior with blue walls, counters and shelves of products">
    <defs>
      <linearGradient id="interiorTones" x1="0" y1="0" x2="0" y2="1">
        <stop offset="0" stop-color="#3e5fa6"/>
        <stop offset=".45" stop-color="#4b68ad"/>
        <stop offset=".6" stop-color="#e9e3d8"/>
        <stop offset=".85" stop-color="#c9b79e"/>
        <stop offset="1" stop-color="#8e8782"/>
      </linearGradient>
    </defs>
    <polygon points="0,64 437,64 392,312 0,312" fill="url(#interiorTones)"/>
  </svg>

  <h2 class="tagline">FEELING BETTER STARTS HERE</h2>

  <div class="mark">
    <span class="mark__dot"></span>
    <span class="mark__name">FERNVALE<br>PHARMACY</span>
  </div>
  <div class="stamp"></div>

  <div class="service service--forget">
    <span class="service__dot"></span>
    <div><p class="service__title">Do you forget taking your medications!</p>
    <p class="service__text">We offer multiple compliance packaging options at no<br>additional cost.</p></div>
  </div>
  <div class="service service--shingles">
    <span class="service__dot"></span>
    <div><p class="service__title">Had shingles before or worried to have it?<br>Travelling soon?</p>
    <p class="service__text">check our vaccinations options!</p></div>
  </div>
  <div class="service service--effects">
    <span class="service__dot"></span>
    <div><p class="service__title">Suffering side effects?</p>
    <p class="service__text">We are experienced to check your medications interactions<br>&amp; different coverage options.</p></div>
  </div>
  <div class="service service--pressure">
    <span class="service__dot"></span>
    <div><p class="service__title">Hard time monitoring your blood pressure?</p>
    <p class="service__text">Trying to stop smoking? we can always help.</p></div>
  </div>

  <div class="footer-contact footer-contact--phone">
    <svg viewBox="0 0 24 24"><path d="M6.6 2.5l3 3.6-1.9 2.4c1.2 2.6 3.2 4.7 5.8 5.9l2.4-1.9 3.6 3-1.8 3.3C10.6 19 5 13.4 3.3 4.3z" fill="#f20000"/><path d="M14 3.5a7 7 0 0 1 6.5 6.5M14 6.5a4 4 0 0 1 3.5 3.5" fill="none" stroke="#f20000" stroke-width="1.6"/></svg>
    <span class="footer-contact__number">604 827 5530</span><span class="footer-contact__note">(call or text)</span>
  </div>
  <div class="footer-contact footer-contact--fax">
    <svg viewBox="0 0 24 24"><rect x="6" y="2" width="12" height="6" fill="#f20000"/><rect x="2" y="8" width="20" height="9" rx="2" fill="#f20000"/><rect x="6" y="14" width="12" height="8" fill="#f20000" stroke="#000" stroke-width="1"/></svg>
    <span class="footer-contact__number">604-827-5532</span>
  </div>
</section>

</body>
</html>
```